Business Card Design

Copperfield Lantern & Spark, Inc. (CLS), located in Memphis, TN began operating on 2003. We are a certified
minority woman-owned business that genuinely takes a vested interest in our customers. We serve utilities,
government, contractors and end user markets in electrical, water, gas and industrial supplies. Our core
competency as a distributor of electrical materials has positioned us to serve business of all size. As your supply
chain partner, we arm you with the resources you need to make your supply chain more efficient. Our team
works with your team on a daily basis to help you solve problems and achieve goals. This team approach has
helped CLS customers to succeed and we can do the same for you.

NAICS Codes:
423610 Electrical Apparatus and Equipment, Wiring Supplies, and Related Equipment Merchant
Wholesalers
423510 Metal Service Centers and Other Metal Merchant Wholesalers
423720 Plumbing and Heating Equipment and Supplies (Hydronics) Merchant Wholesalers

Certifications
MBE (KRVPQAL, State of Tennessee Up-MRX and FJW), WBE (HQOLT),
WOSB, DOT (TDOT, MDOT, ALDOT, SCDOT, NCDOT, and VDOT), LOSB,
SBE, and LSB Certified
Some of Our Products Include:
. Boxes & Covers
. Conduit & Raceway
. Fittings
. Fuses
. Lamp & Ballasts
. Lighting Controls & Timers
. Lighting Fixtures
. Personal Safety
. Pipes
. Power Distribution
. Terminations Ground & Splices
. Tools & Testers
. Wire, Cords & Cable
. Wiring Devices
. Valves

Industry/Entity Type

Business

Contact Information for Business Card

Marianne T. Holloway - President/CEO
4728 Quillon Ave., Memphis, TN 38127
901-555-0147 office, 901-555-0182 fax, 901-555-0163 cell
mtholloway@clsllc-example.com - www.clsincorp-example.com

```html
<!DOCTYPE html>
<html lang="en">
<head>
<meta charset="utf-8">
<title>Copperfield Lantern &amp; Spark – Business Card</title>
<link rel="stylesheet" href="https://fonts.googleapis.com/css2?family=Open+Sans:wght@400;600&display=swap">
<style>
  :root {
    --olive: #b1ae32;
    --ink: #111111;
    --paper: #ffffff;
    --backdrop: #ecebe8;
    --card-w: 918px;
    --card-h: 524px;
  }
  * { box-sizing: border-box; margin: 0; padding: 0; }
  html, body {
    width: 1189px; height: 1200px; overflow: hidden;
    background: var(--backdrop);
    font-family: "Open Sans", Arial, sans-serif;
    color: var(--ink);
  }
  .card {
    position: absolute; left: 136px;
    width: var(--card-w); height: var(--card-h);
    background: var(--paper);
    box-shadow: 0 3px 10px rgba(0,0,0,.18);
    overflow: hidden;
  }
  .card--front { top: 45px; }
  .card--back { top: 623px; }

  .wordmark {
    position: absolute;
    display: flex; align-items: center; gap: 14px;
    text-transform: uppercase; font-weight: 400; color: var(--ink);
    line-height: 1.05; letter-spacing: .04em;
  }
  .wordmark__mark { background: var(--olive); flex: none; }
  .wordmark__name span { display: block; }
  .wordmark__name span + span { padding-left: 1.1em; }

  .card--front .wordmark { left: 36px; top: 172px; font-size: 40px; }
  .card--front .wordmark__mark { width: 34px; height: 34px; }
  .card--back .wordmark { left: 50%; top: 50%; transform: translate(-50%, -50%); font-size: 54px; }
  .card--back .wordmark__mark { width: 44px; height: 44px; }

  .contact {
    position: absolute; right: 33px; top: 30px;
    text-align: right;
  }
  .contact__name { color: var(--olive); font-size: 39px; font-weight: 400; line-height: 1.2; }
  .contact__title { font-size: 25px; line-height: 1.2; }
  .contact__address { margin-top: 16px; font-size: 24px; line-height: 40px; font-style: normal; }
  .contact__list { list-style: none; margin-top: 18px; }
  .contact__item {
    display: flex; justify-content: flex-end; align-items: center; gap: 26px;
    font-size: 24px; line-height: 37px;
  }
  .contact__icon { width: 22px; height: 22px; flex: none; }

  .card__wave { position: absolute; left: 0; bottom: 0; width: 100%; height: 110px; }
</style>
</head>
<body>

<section class="card card--front" aria-label="Business card front">
  <div class="wordmark">
    <span class="wordmark__mark"></span>
    <div class="wordmark__name"><span>Copperfield</span><span>Lantern &amp; Spark</span></div>
  </div>

  <div class="contact">
    <h1 class="contact__name">Marianne T. Holloway</h1>
    <p class="contact__title">President/CEO</p>
    <address class="contact__address">4728 Quillon Ave.,<br>Memphis, TN 38127</address>
    <ul class="contact__list">
      <li class="contact__item">901-555-0163
        <svg class="contact__icon" viewBox="0 0 22 22"><rect width="22" height="22" fill="var(--olive)"/><rect x="7" y="3" width="8" height="16" rx="1.5" fill="#fff"/><rect x="8.5" y="5" width="5" height="5" fill="var(--olive)"/></svg></li>
      <li class="contact__item">901-555-0147
        <svg class="contact__icon" viewBox="0 0 22 22"><rect width="22" height="22" fill="var(--olive)"/><path d="M7 4l3 3-1.5 2c1 2 2.5 3.5 4.5 4.5L15 12l3 3-2 3C10 17 5 12 4 6z" fill="#fff"/></svg></li>
      <li class="contact__item">901-555-0182
        <svg class="contact__icon" viewBox="0 0 22 22"><rect width="22" height="22" fill="var(--olive)"/><rect x="7" y="4" width="8" height="5" fill="#fff"/><rect x="4" y="9" width="14" height="6" fill="#fff"/><rect x="7" y="14" width="8" height="4" fill="#fff"/></svg></li>
      <li class="contact__item">mtholloway@clsllc-example.com
        <svg class="contact__icon" viewBox="0 0 22 22"><rect width="22" height="22" fill="var(--olive)"/><rect x="4" y="6" width="14" height="10" fill="#fff"/><path d="M4 6l7 6 7-6" fill="none" stroke="var(--olive)" stroke-width="1.3"/></svg></li>
      <li class="contact__item">www.clsincorp-example.com
        <svg class="contact__icon" viewBox="0 0 22 22"><rect width="22" height="22" fill="var(--olive)"/><circle cx="11" cy="11" r="7" fill="#fff"/><path d="M8 7c2 1 1 3 3 4s0 4 2 5M13 6c1 2 3 2 4 4" fill="none" stroke="var(--olive)" stroke-width="1.5"/></svg></li>
    </ul>
  </div>

  <svg class="card__wave" viewBox="0 0 918 110" preserveAspectRatio="none" aria-hidden="true">
    <path d="M0 0 C120 -4 230 40 380 48 C520 56 640 30 740 24 C640 38 520 68 380 70 C230 72 120 40 0 38 Z" fill="var(--olive)"/>
    <path d="M0 43 C120 45 230 78 380 78 C560 78 720 28 830 28 C870 28 900 38 918 48 L918 110 L0 110 Z" fill="var(--ink)"/>
  </svg>
</section>

<section class="card card--back" aria-label="Business card back">
  <div class="wordmark">
    <span class="wordmark__mark"></span>
    <div class="wordmark__name"><span>Copperfield</span><span>Lantern &amp; Spark</span></div>
  </div>
</section>

</body>
</html>
```